Tumbleroo Childcare centre needs a new LED outdoor banner

We need a new outdoor banner for our pre-school. It needs to be around 2440 mm x 1220 mm. It will be lit at night so I need it to stand out. I'm looking for a modern upbeat design. It will have my logo in the middle which is a graduation teddy bear with our name and phone number on it. I'm happy to experiment with different design options as mine is 20 years old. It needs to be colorful, inviting and very "in your face" and child friendly. It will be located near the fence of the property so it will be seen by cars driving by at a speed of around 50KM/H. So it needs to be clear, big bold fonts and bright colors. Thank you!

```html
<!DOCTYPE html>
<html lang="en">
<head>
<meta charset="utf-8">
<title>Tumbleroo Childcare Centre – Outdoor Banner</title>
<link href="https://fonts.googleapis.com/css2?family=Fredoka:wght@500;700&family=Montserrat:wght@800&display=swap" rel="stylesheet">
<style>
  :root {
    --page-bg: #e6e6e6;
    --sun-yellow: #fcd406;
    --deep-blue: #0066b8;
    --bright-cyan: #3fd0f0;
    --sky-light: #d9f1fb;
    --sky-mid: #8fd3ea;
    --rainbow-peach: #f7b98a;
    --rainbow-rose: #ef8a8f;
    --hot-pink: #ec008c;
    --ink: #0a0a0a;
    --white: #ffffff;
    --teddy-brown: #8a6a55;
  }
  * { box-sizing: border-box; margin: 0; padding: 0; }
  html, body {
    width: 1200px; height: 1200px; overflow: hidden;
    background: var(--page-bg);
  }
  .banner {
    position: absolute;
    left: 40px; top: 320px;
    width: 1120px; height: 560px;
    overflow: hidden;
    background: var(--sun-yellow);
  }
  .banner-bg { position: absolute; inset: 0; width: 1120px; height: 560px; }
  .brand {
    position: absolute;
    left: 0; width: 1120px; top: 40px;
    text-align: center;
    font-family: "Fredoka", sans-serif;
    font-weight: 700;
    color: var(--hot-pink);
    line-height: 1;
  }
  .brand-mark {
    display: block;
    width: 96px; height: 96px;
    margin: 0 auto 10px;
    border-radius: 50%;
    background: var(--teddy-brown);
  }
  .brand-name { display: block; font-size: 104px; letter-spacing: -1px; }
  .brand-sub { display: block; font-size: 62px; margin-top: 6px; }
  .hours-pill {
    position: absolute;
    left: 205px; top: 377px;
    width: 710px; height: 74px;
    background: var(--hot-pink);
    border: 3px solid var(--ink);
    border-radius: 16px;
    color: var(--white);
    font-family: "Fredoka", sans-serif;
    font-weight: 500;
    font-size: 46px;
    display: flex; align-items: center; justify-content: center;
    white-space: nowrap;
  }
  .address {
    position: absolute;
    left: 0; width: 1120px; top: 458px;
    text-align: center;
    font-family: "Montserrat", sans-serif;
    font-weight: 800;
    font-size: 25px;
    color: var(--ink);
    white-space: nowrap;
  }
  .phone {
    position: absolute;
    left: 0; width: 1120px; top: 494px;
    text-align: center;
    font-family: "Montserrat", sans-serif;
    font-weight: 800;
    font-size: 46px;
    color: var(--ink);
    letter-spacing: 1px;
  }
</style>
</head>
<body>
  <div class="banner">
    <svg class="banner-bg" viewBox="0 0 1120 560" aria-hidden="false">
      <defs>
        <linearGradient id="sky-fill" x1="0" y1="0" x2="1" y2="0.3">
          <stop offset="0" stop-color="var(--sky-mid)"/>
          <stop offset="0.35" stop-color="#9fc98a"/>
          <stop offset="0.65" stop-color="var(--rainbow-peach)"/>
          <stop offset="0.85" stop-color="var(--rainbow-rose)"/>
          <stop offset="1" stop-color="var(--sky-light)"/>
        </linearGradient>
        <linearGradient id="swoosh-fill" x1="0" y1="0" x2="1" y2="1">
          <stop offset="0" stop-color="var(--sky-mid)"/>
          <stop offset="1" stop-color="var(--white)"/>
        </linearGradient>
      </defs>
      <path class="left-swoosh" fill="url(#swoosh-fill)"
            d="M70 0 L95 0 C80 180 110 350 255 560 L75 560 C45 380 40 180 70 0 Z"/>
      <g class="rainbow-sky" role="img" aria-label="Pastel rainbow arcs over a pale blue sky with small white stars">
        <path fill="url(#sky-fill)"
              d="M120 0 L1120 0 L1120 277 C960 360 760 395 560 392 C380 390 250 330 190 250 C150 190 125 100 120 0 Z"/>
      </g>
      <path class="cyan-stripe" fill="var(--bright-cyan)"
            d="M58 0 L70 0 C45 180 50 380 80 560 L70 560 C38 380 35 180 58 0 Z"/>
      <path class="blue-band" fill="var(--deep-blue)"
            d="M0 0 L58 0 C35 180 38 380 70 560 L0 560 Z"/>
    </svg>

    <div class="brand">
      <span class="brand-mark"></span>
      <span class="brand-name">Tumbleroo</span>
      <span class="brand-sub">Childcare Centre</span>
    </div>

    <div class="hours-pill">0 - 6 years | 7.30am - 5.30pm</div>
    <p class="address">48 Wattle Lane, Brookvale Heights NSW 2150</p>
    <p class="phone">02 9555 0148</p>
  </div>
</body>
</html>
```